webdesign for a spectacles/glasses designer

Hello,

Someone in my village designs his own spectacles/eyeglasses.

For this I need a design that looks better than my poor design skills ;o)

The site is based around collections, subcollections and the actual items.

So we need a design that lists these in a nice way, worst case on seperate pages.

Here you can find the working material...

https://www.filevault-example.com/s/q8rtk2mzp4vn71c/ArtHive.zip

keep an eye on the product_tree file.

first level is the collection name
2nd is the model group
3rd is the model (on most of them it's just a different color of the same base model)

I added a seperate contact info file (line is too slow to reupload 60Mb again :( )

https://dl.filevault-example.com/u/31946082/Marten/contact.zip

I think I forgot to mention that it will be a shop like site to present his products,
altho I will add a cart system there won't be a payment system linked to it as
people who place orders will get contacted with payment instructions.
Updates

In the zipfile /Logo/logo_mistral_font.psd is the main logo
(you need to change character spacing to 1 to get rid of the spacing gaps)

the other one is only a collection logo

Target Market(s)

Plain customers and his resellers.

Industry/Entity Type

Shop

Requirements
Must have
• - a design that suits responsive behaviour (via the 960 grid)
- a menu is always handy (home, about, collections, contact)
- highlighted area/slider to highlight his sunglasses over glasses thingy
- featured products (newly added or promotional stuff)

there is a lot of pretty pictures to be supplied so do what you think is best

Nice to have
• a roll over zoom with selectable thumbnails or a plain gallery with full picture display at the product page.

maybe a drop down menu for the collection part (I will supply a screenshot of the backend structure)

```html
<!DOCTYPE html>
<html lang="en">
<head>
<meta charset="utf-8">
<title>Vellano – Eyewear Shop</title>
<link rel="stylesheet" href="https://fonts.googleapis.com/css2?family=Arimo:wght@400;700&family=Arvo&family=PT+Sans&display=swap">
<style>
:root{
  --backdrop:#1c1d1f;
  --page:#ffffff;
  --accent:#f47c62;
  --hero-panel:#4f4a48;
  --ink:#222222;
  --topbar:#111111;
  --footer:#17191b;
  --footer-link:#e0352b;
  --note:#ffffff;
  --pay:#4d94f2;
  --tile-light:#f6f6f6;
  --tile-dark:#e3e3e3;
}
*{box-sizing:border-box;margin:0;padding:0}
html,body{width:1200px;height:1000px;overflow:hidden;background:var(--backdrop);font-family:"Arimo",Arial,sans-serif;color:var(--ink)}
.canvas{position:relative;width:1200px;height:1000px}
.abs{position:absolute}

/* annotations */
.note{position:absolute;background:var(--note);font-family:"PT Sans",sans-serif;font-size:17.5px;line-height:21.5px;color:#333;padding:8px}

/* header */
.header{left:230px;top:0;width:718px;height:80px;background:var(--page)}
.brand{left:10px;top:14px;font-family:"Arvo",serif;font-size:44px;color:#111}
.nav{left:254px;top:15px;display:flex;gap:25px;font-size:12px;letter-spacing:.3px}
.nav span{display:inline-flex;align-items:center;gap:3px}
.social{left:642px;top:17px;display:flex;gap:7px}
.social i{display:block;width:8px;height:8px;border-radius:50%;background:#555}
.accent-rule{left:230px;top:80px;width:718px;height:8px;background:var(--accent)}
.topbar{left:230px;top:88px;width:718px;height:16px;background:var(--topbar);color:#fff;font-size:7px;font-weight:700}
.topbar span{position:absolute;top:4px}

/* hero */
.hero-panel{left:230px;top:104px;width:394px;height:226px;background:var(--hero-panel);color:#fff}
.hero-panel h1{position:absolute;left:23px;top:34px;font-weight:400;font-size:22px;letter-spacing:1px}
.hero-panel p{position:absolute;left:23px;top:67px;font-size:11px;line-height:13px;letter-spacing:.85px}
.btn{background:var(--accent);color:#fff;font-size:10px;display:flex;align-items:center;justify-content:center;letter-spacing:.3px}
.hero-panel .btn{position:absolute;left:23px;top:132px;width:72px;height:24px;font-size:11px}
.hero-photo{left:624px;top:104px;width:324px;height:226px;
  background:
    radial-gradient(ellipse 90px 110px at 52% 42%,#d9c08e 0,#c2a677 45%,rgba(194,166,119,0) 75%),
    linear-gradient(180deg,rgba(0,0,0,0) 70%,#1d1a18 100%),
    linear-gradient(135deg,#8d8c8a,#6f6e6c 55%,#4a4644)}

/* featured */
.section{left:230px;width:718px;background:var(--page)}
.featured-title{left:12px;top:6px;font-family:"Arvo",serif;font-size:12px;color:#333}
.carousel{left:0;top:27px;width:718px;height:90px;display:flex}
.frame-tile{width:90px;height:90px;border-right:1px solid #fff;
  background:linear-gradient(180deg,var(--tile-light) 0,var(--tile-light) 36%,var(--frame) 44%,var(--frame-soft) 50%,var(--frame) 56%,#f1f1f1 64%,var(--tile-dark) 100%)}
.arrow{width:22px;height:22px;border-radius:50%;background:#333;display:flex;align-items:center;justify-content:center}
.featured-btns{left:14px;top:121px;display:flex;gap:32px}
.featured-btns .btn{width:58px;height:19px;font-size:9.5px}

/* story */
.story h2{position:absolute;left:16px;top:7px;font-weight:400;font-size:15px;letter-spacing:.8px;color:#3a2a24}
.story-photo{left:15px;top:32px;width:160px;height:160px;
  background:
    radial-gradient(ellipse 120px 60px at 40% 40%,#5a3626 0,#7a4b33 40%,rgba(122,75,51,0) 75%),
    linear-gradient(135deg,#f7f7f7,#ece8e5 55%,#d8cfc9)}
.story-text{left:188px;top:43px;width:514px;font-family:"PT Sans",sans-serif;font-size:9.6px;line-height:14px}
.story .btn{position:absolute;left:189px;top:159px;width:60px;height:20px}

/* latest */
.latest h2{position:absolute;left:156px;top:4px;font-family:"Arvo",serif;font-weight:400;font-size:17px;color:#333}
.switch{left:486px;top:10px;font-size:7px;display:flex;gap:3px;align-items:center;color:#444}
.switch i{display:block;width:9px;height:7px;border:1px solid #999;background:#ddd}
.latest-rule{left:0;top:30px;width:718px;height:1px;background:#f3b3a5}
.latest-intro{left:156px;top:43px;font-size:7px;color:#444}
.latest-grid{left:6px;top:61px;display:flex;gap:11px}
.latest-grid .frame-tile{width:92px;height:91px;border:1px solid #ddd;border-bottom:2px solid var(--accent)}

/* footer */
.footer{left:230px;top:835px;width:485px;height:90px;background:var(--footer)}
.col{position:absolute;top:8px;width:138px;font-size:10px;color:#fff}
.col h3{font-size:10px;font-weight:400;padding-bottom:6px;border-bottom:1px solid #4a7a8a}
.col ul{list-style:none;margin-top:9px}
.col li{color:var(--footer-link);font-size:7px;font-weight:700;line-height:12.5px}
.payment{left:741px;top:851px;width:195px;height:64px;background:var(--pay);color:#fff;font-family:"PT Sans",sans-serif;font-size:27px;display:flex;align-items:center;justify-content:center}
.bottom{left:230px;top:936px;width:722px;height:64px;background:var(--page)}
.bottom-links{position:absolute;left:0;right:0;top:12px;text-align:center;font-family:"Arvo",serif;font-size:9.4px;color:#333}
.to-top{left:690px;top:37px;width:20px;height:20px;border-radius:3px;background:#e65c5c;display:flex;align-items:center;justify-content:center}
</style>
</head>
<body>
<div class="canvas">

  <div class="note" style="left:24px;top:43px;width:178px;height:155px;padding-top:26px">Logo size can change<br>Logo can be on<br>Right or Left or<br>Middle.<br>Nav can also change.</div>
  <div class="note" style="left:998px;top:20px;width:178px;height:154px;padding-top:19px;padding-left:13px">The images can all be changed.<br>The fonts too.<br>And the colours.<br>All can be changed.</div>
  <div class="note" style="left:998px;top:656px;width:178px;height:155px;padding-top:40px;padding-left:10px">This footer area can stay or go. Or change colours, fonts etc.</div>
  <svg class="abs" style="left:940px;top:800px" width="80" height="90" viewBox="0 0 80 90"><line x1="72" y1="4" x2="8" y2="84" stroke="#555" stroke-width="6"/><polygon points="3,88 5,78 13,84" fill="#555"/></svg>

  <header class="abs header">
    <div class="abs brand">Vellano</div>
    <nav class="abs nav">
      <span>Home</span>
      <span>About <svg width="6" height="4"><path d="M0 0L3 3L6 0" fill="none" stroke="#222"/></svg></span>
      <span>Collections <svg width="6" height="4"><path d="M0 0L3 3L6 0" fill="none" stroke="#222"/></svg></span>
      <span>Contact</span>
    </nav>
    <div class="abs social"><i></i><i></i><i></i></div>
  </header>
  <div class="abs accent-rule"></div>
  <div class="abs topbar">
    <span style="left:7px">Search...</span>
    <svg class="abs" style="left:112px;top:4px" width="8" height="8"><circle cx="3" cy="3" r="2.3" stroke="#fff" fill="none"/><line x1="5" y1="5" x2="7.5" y2="7.5" stroke="#fff"/></svg>
    <span style="left:128px">Default welcome msg!</span>
    <span style="left:460px">Cart (0 items)</span>
    <span style="left:521px">Log In</span>
    <span style="left:559px">Sign Up</span>
    <span style="left:603px">Text Size&nbsp;&nbsp; A&nbsp; <b style="font-size:9px">A</b></span>
  </div>

  <section class="abs hero-panel">
    <h1>AMAZING HEADING</h1>
    <p>Lorem&nbsp; Ipsum and some very great words would go here<br>It would have a great impact on your site.<br>Users will flock and buy!</p>
    <div class="btn">Read More</div>
  </section>
  <div class="abs hero-photo" role="img" aria-label="Model with blond hair wearing dark sunglasses"></div>

  <section class="abs section" style="top:330px;height:145px">
    <div class="abs featured-title">Featured Products</div>
    <div class="abs carousel">
      <div class="frame-tile" style="--frame:#c98a92;--frame-soft:#e8c4c8" role="img" aria-label="Rose metal eyeglass frame"></div>
      <div class="frame-tile" style="--frame:#c9825a;--frame-soft:#e9c2a8" role="img" aria-label="Copper metal eyeglass frame"></div>
      <div class="frame-tile" style="--frame:#9a92c8;--frame-soft:#cfcae6" role="img" aria-label="Lilac metal eyeglass frame"></div>
      <div class="frame-tile" style="--frame:#a88670;--frame-soft:#d8c6b8" role="img" aria-label="Bronze metal eyeglass frame"></div>
      <div class="frame-tile" style="--frame:#cf7a4e;--frame-soft:#ecbda2" role="img" aria-label="Orange metal eyeglass frame"></div>
      <div class="frame-tile" style="--frame:#8a8a8e;--frame-soft:#c9c9cc" role="img" aria-label="Gunmetal eyeglass frame"></div>
      <div class="frame-tile" style="--frame:#9a8e88;--frame-soft:#d2cbc7" role="img" aria-label="Taupe metal eyeglass frame"></div>
      <div class="frame-tile" style="--frame:#a4a4a8;--frame-soft:#d6d6d8" role="img" aria-label="Silver metal eyeglass frame"></div>
    </div>
    <div class="abs arrow" style="left:3px;top:62px"><svg width="6" height="8"><path d="M5 0L1 4L5 8" fill="none" stroke="#fff" stroke-width="1.5"/></svg></div>
    <div class="abs arrow" style="left:693px;top:62px"><svg width="6" height="8"><path d="M1 0L5 4L1 8" fill="none" stroke="#fff" stroke-width="1.5"/></svg></div>
    <div class="abs featured-btns">
      <div class="btn">Read More</div><div class="btn">Read More</div><div class="btn">Read More</div><div class="btn">Read More</div>
      <div class="btn">Read More</div><div class="btn">Read More</div><div class="btn">Read More</div><div class="btn">Read More</div>
    </div>
  </section>

  <section class="abs section story" style="top:475px;height:205px;border-top:1px solid #ddd">
    <h2>A Big Long Title of Meaning Can Go Here</h2>
    <div class="abs story-photo" role="img" aria-label="Close-up of a tortoiseshell eyeglass frame"></div>
    <p class="abs story-text">Lorem Ipsum is simply dummy text of the printing and typesetting industry. Lorem Ipsum has been the industry's standard dummy text ever since the 1500s, when an unknown printer took a galley of type and scrambled it to make a&nbsp; type specimen book. It has survived not only five centuries, but also the leap into electronic typesetting, remaining essentially unchanged. It was popularised in the 1960s with the release of Typeleaf sheets containing<br>Lorem Ipsum passages, and more recently with desktop publishing software like Quillset Composer including versions of Lorem Ipsum.<br>remaining essentially unchanged. It was popularised in the 1960s with the release of Typeleaf sheets containing.</p>
    <div class="btn">Read More</div>
  </section>

  <section class="abs section latest" style="top:680px;height:155px">
    <h2>Latest products</h2>
    <div class="abs switch"><i></i><i></i>&nbsp;Switch View</div>
    <div class="abs latest-rule"></div>
    <div class="abs latest-intro">Check out a selection of our items currently for sale:</div>
    <div class="abs latest-grid">
      <div class="frame-tile" style="--frame:#9a92c8;--frame-soft:#d2cde8" role="img" aria-label="Lilac metal eyeglass frame"></div>
      <div class="frame-tile" style="--frame:#9a92c8;--frame-soft:#d2cde8" role="img" aria-label="Lilac metal eyeglass frame"></div>
      <div class="frame-tile" style="--frame:#9a92c8;--frame-soft:#d2cde8" role="img" aria-label="Lilac metal eyeglass frame"></div>
      <div class="frame-tile" style="--frame:#9a92c8;--frame-soft:#d2cde8" role="img" aria-label="Lilac metal eyeglass frame"></div>
      <div class="frame-tile" style="--frame:#9a92c8;--frame-soft:#d2cde8" role="img" aria-label="Lilac metal eyeglass frame"></div>
      <div class="frame-tile" style="--frame:#9a92c8;--frame-soft:#d2cde8" role="img" aria-label="Lilac metal eyeglass frame"></div>
      <div class="frame-tile" style="--frame:#9a92c8;--frame-soft:#d2cde8" role="img" aria-label="Lilac metal eyeglass frame"></div>
    </div>
  </section>

  <footer class="abs footer">
    <div class="col" style="left:19px"><h3>New Products</h3><ul><li>Lorem</li><li>Ipsum</li><li>Lorem Ipsum</li><li>Ipsum Lorem</li></ul></div>
    <div class="col" style="left:180px"><h3>Another Title</h3><ul><li>Lorem</li><li>Ipsum</li><li>Lorem Ipsum</li><li>Ipsum Lorem</li></ul></div>
    <div class="col" style="left:342px"><h3>Another Title</h3><ul><li>Lorem</li><li>Ipsum</li><li>Lorem Ipsum</li><li>Ipsum Lorem</li></ul></div>
  </footer>
  <div class="abs payment">Payment Logo</div>

  <div class="abs bottom">
    <div class="bottom-links">Cart (0 items)&nbsp; /&nbsp; Customer Service&nbsp; /&nbsp; Privacy Policy&nbsp; /&nbsp; Site Map&nbsp; /&nbsp; Search Terms&nbsp; /&nbsp; Advanced Search&nbsp; /&nbsp; Contact Us&nbsp; /</div>
    <div class="abs to-top"><svg width="8" height="5"><path d="M0 5L4 1L8 5" fill="none" stroke="#fff" stroke-width="1.5"/></svg></div>
  </div>

</div>
</body>
</html>
```